Business card design needed

Family General Practitioner/ Family Physician.
Logo is the logo of the Crestmoor Guild of Family Clinicians Australia
http://kvplm.tarevo.edu.au/PictureGallery/logos/pages/CGFC%20logo_jpg.htm

Reason: Just a bit more time to make changes and the weekend for me to look at things closely and to choose. Thanks, Lumi

Thanks for all the submissions. So many of them are really works of art. Not one of them are not good. The ones that I am eliminating are the ones that I think are not suitable for me personally only, and because if I don't, it makes it very difficult to decide as many of you are also sending me slight variations of a card. I have just decided to choose a second place card too. Can't thank you all enough. Good luck, Lumi. P.S - Working today till 10 pm as the card says :-), so probably won't be able to give a feedback till late Saturday night or Sunday morning here in Sydney, Australia. 

Reason: Just added a second place to the budget and realised that Australia is ahead of the rest of the world in the time zone (only :-) - don't want to offend anyone or start a debate!! ) , so Monday deadline will mean it will be a weekend for the rest of the world. Just wanted to give everyone more time to submit their best, especially since I will be picking a second card too. Can't thank everyone enough for the submissions. P.S - Not keen on photos on the card.

Contact Information for Business Card

Dr. Lumi Harcourt M.B.B.S., F.C.G.F.C
Family General Practitioner
Address, timings, phone and fax number on the back.

Requirements
Must have
• Timings
Mon 7 am - 7 pm
Tues 7 am - 12 pm
Wed 7 am - 10 pm
Thurs 7 am - 12 pm
Fri 7 am - 8 pm
Sat 8 am - 10 pm
Sun - Off

```html
<!DOCTYPE html>
<html lang="en">
<head>
<meta charset="utf-8">
<title>Dr. Lumi Harcourt – Business Card</title>
<link rel="stylesheet" href="https://fonts.googleapis.com/css2?family=Lato:wght@400;700;900&display=swap">
<style>
  :root {
    --backdrop: #1f4a78;
    --card: #ffffff;
    --pink: #ec1e79;
    --pink-2: #ef4a8c;
    --pink-3: #f06a9d;
    --pink-4: #f28aae;
    --ink: #231f20;
    --ink-maroon: #3a0a12;
    --grey: #6d6e71;
    --light-grey: #e3e3e3;
    --sky: #6dcff6;
    --blush: #f7c5da;
  }
  * { box-sizing: border-box; margin: 0; padding: 0; }
  html, body { width: 1200px; height: 720px; overflow: hidden; }
  body {
    background: var(--backdrop);
    font-family: "Lato", Arial, sans-serif;
    position: relative;
  }
  .card {
    position: absolute;
    background: var(--card);
    width: 530px;
    height: 310px;
  }

  /* Front */
  .card-front {
    left: 50px; top: 40px;
    clip-path: polygon(40px 0, 100% 0, 100% 82%, 92% 100%, 0 100%, 0 16%);
  }
  .family-illustration {
    position: absolute;
    left: 40px; top: 30px;
    width: 370px; height: 190px;
    border-radius: 50%;
    background:
      radial-gradient(circle at 45% 55%, var(--light-grey) 0 30%, transparent 31%),
      radial-gradient(circle at 20% 40%, var(--blush) 0 8%, transparent 9%),
      radial-gradient(circle at 80% 30%, var(--sky) 0 7%, transparent 8%),
      linear-gradient(160deg, #eaf7fd, #fde8f1 60%, #f0f0f0);
  }
  .guild-name {
    position: absolute;
    right: 34px; top: 22px;
    display: flex; align-items: center; gap: 6px;
    font-weight: 700; font-size: 15px; color: var(--ink);
  }
  .guild-name .dot {
    width: 12px; height: 12px; border-radius: 50%; background: var(--pink);
  }
  .identity {
    position: absolute;
    left: 150px; top: 226px;
    text-align: right;
    width: 250px;
  }
  .doctor-name {
    font-size: 24px; font-weight: 900; letter-spacing: .3px; line-height: 1;
    color: var(--ink);
  }
  .doctor-name .first { color: var(--pink); }
  .credentials {
    font-size: 12px; color: var(--grey); margin-top: 4px; letter-spacing: .5px;
  }
  .role {
    font-size: 13px; color: var(--ink); margin-top: 3px; letter-spacing: .3px;
  }
  .role strong { font-weight: 900; }

  /* Back */
  .card-back {
    left: 600px; top: 370px;
    width: 560px;
    clip-path: polygon(0 0, 100% 0, 100% 84%, 95% 100%, 0 100%, 0 14%);
  }
  .bubble-accent {
    position: absolute;
    right: 40px; top: 0;
    width: 280px; height: 48px;
    background: linear-gradient(90deg, #eaf7fd, #fde8f1 50%, #d9d9d9);
    border-radius: 0 0 40px 40px;
  }
  .label {
    display: inline-block;
    background: var(--pink);
    color: #fff;
    font-weight: 700;
    font-size: 15px;
    padding: 5px 8px;
    width: 108px;
  }
  .address { position: absolute; left: 22px; top: 52px; }
  .address p {
    margin-top: 10px;
    color: var(--pink);
    font-weight: 700;
    font-size: 14px;
    line-height: 18px;
  }
  .contact { position: absolute; left: 22px; top: 194px; }
  .contact p {
    margin-top: 10px;
    color: var(--pink);
    font-weight: 700;
    font-size: 14px;
    line-height: 19px;
  }
  .baby-icon {
    position: absolute;
    left: 170px; top: 200px;
    width: 75px; height: 96px;
    border-radius: 40px;
    background: linear-gradient(180deg, #ececec, #d8d8d8);
  }
  .hours {
    position: absolute;
    left: 258px; top: 52px;
    border-collapse: separate;
    border-spacing: 3px 6px;
  }
  .hours th, .hours td {
    height: 29px;
    font-size: 14.5px;
    text-align: left;
    padding: 0 8px;
    color: #fff;
    white-space: nowrap;
  }
  .hours th { background: var(--ink); font-weight: 400; width: 106px; }
  .hours td { width: 160px; }
  .hours tr:nth-child(1) td, .hours tr:nth-child(2) td { background: var(--pink); }
  .hours tr:nth-child(3) td, .hours tr:nth-child(4) td { background: var(--pink-2); }
  .hours tr:nth-child(5) td { background: var(--pink-3); }
  .hours tr:nth-child(6) td { background: var(--pink-4); }
  .hours tr:nth-child(7) th { background: var(--ink-maroon); }
  .hours tr:nth-child(7) td { background: #f399b9; }
</style>
</head>
<body>

<section class="card card-front">
  <div class="family-illustration" role="img" aria-label="Illustration of a stick-figure family among pink, blue and grey bubbles"></div>
  <div class="guild-name"><span class="dot"></span>CGFC</div>
  <div class="identity">
    <h1 class="doctor-name"><span class="first">DR. LUMI</span> HARCOURT</h1>
    <p class="credentials">M.B.B.S. , F.C.G.F.C</p>
    <p class="role">FAMILY <strong>GENERAL PRACTITIONER</strong></p>
  </div>
</section>

<section class="card card-back">
  <div class="bubble-accent" role="img" aria-label="Cluster of pink, blue and grey bubbles"></div>

  <div class="address">
    <span class="label">ADDRESS</span>
    <p>Upper Level,<br>Marlowe Court,<br>Brindle Park Shopping Centre<br>Fernleigh Hill,<br>NSW 2199</p>
  </div>

  <div class="contact">
    <span class="label">CONTACT</span>
    <p>T : 02-5550-1400<br>F : 02-5550-1433</p>
  </div>

  <div class="baby-icon" role="img" aria-label="Line illustration of a swaddled baby"></div>

  <table class="hours">
    <tr><th>MONDAY</th><td>07:00 AM - 07:00 PM</td></tr>
    <tr><th>TUESDAY</th><td>07:00 AM - 12:00 PM</td></tr>
    <tr><th>WEDNESDAY</th><td>07:00 AM - 10:00 PM</td></tr>
    <tr><th>THURSDAY</th><td>07:00 AM - 12:00 PM</td></tr>
    <tr><th>FRIDAY</th><td>07:00 AM - 08:00 PM</td></tr>
    <tr><th>SATURDAY</th><td>08:00 AM - 10:00 PM</td></tr>
    <tr><th>SUNDAY</th><td>OFF</td></tr>
  </table>
</section>

</body>
</html>
```